Non-profit sports organization needs templates for Word and InDesign

"Pelo Minis" is a non-profit organization in Winterthur, which supports the recruitment of young talent by the handball clubs in Winterthur. Every year we run several camps, a tournament for schoolchildren and several handball lessons at school.
During these activities there are always written information. So far we have not given much thought to the design. But since we think that a professional design will also lead to more interaction, we now turn to you as a designer.

For the communication with partners, sponsors, patrons, etc. we need a uniform appearance. Since different departments are currently working with different programs, we need a template for letters and documentation for Word and InDesign.

We will need the documentation template for project descriptions, information, etc.
The letter templates are needed to contact sponsors, authorities, patrons, etc.

Both the letter template and the documentation template should look modern. The design should be based on the existing flyers. Otherwise we have no other requirements so far.

Homepage: www.pelo-minis.ch

Target Market(s)

Letters, documentation or information to authorities, sponsors, associations, patrons, members, participants, etc.

Requirements
Must have
• In addition to the design, the templates should also contain a concept for titles, paragraphs, lists, etc. (colors / fonts / ...)

Word and Indesign templates

```html
<!DOCTYPE html>
<html lang="en">
<head>
<meta charset="utf-8">
<title>Pelo Minis – Documentation Page</title>
<link href="https://fonts.googleapis.com/css2?family=Arimo:ital,wght@0,400;0,700;1,400&display=swap" rel="stylesheet">
<style>
  :root {
    --brand-red: #e8150c;
    --brand-blue: #3b9ad6;
    --ink: #1a1a1a;
    --paper: #ffffff;
    --rule: #222222;
  }
  * { box-sizing: border-box; margin: 0; padding: 0; }
  html, body { width: 848px; height: 1200px; overflow: hidden; background: var(--paper); }
  body { font-family: "Arimo", Arial, sans-serif; color: var(--ink); }
  .page { position: relative; width: 848px; height: 1200px; overflow: hidden; }

  .header-rule { position: absolute; height: 2px; }
  .header-rule.red { top: 93px; background: var(--brand-red); }
  .header-rule.blue { top: 101px; background: var(--brand-blue); }
  .header-rule.left { left: 0; width: 348px; }
  .header-rule.right { left: 491px; width: 357px; }

  .brand {
    position: absolute; left: 349px; width: 142px; top: 86px;
    display: flex; align-items: center; justify-content: center; gap: 6px;
  }
  .brand-dot { width: 10px; height: 10px; border-radius: 50%; background: var(--brand-blue); }
  .brand-name { font-size: 20px; font-weight: 700; color: var(--brand-red); white-space: nowrap; }

  .block { position: absolute; left: 56px; width: 740px; }
  .doc-title { top: 166px; text-align: center; color: var(--brand-red); font-size: 23px; font-weight: 700; }
  .doc-subtitle { top: 213px; text-align: center; color: var(--brand-blue); font-size: 17px; font-weight: 700; }

  .section-heading {
    text-align: center; font-size: 15.5px; font-weight: 700;
    text-decoration: underline; text-underline-offset: 2px; line-height: 20px; margin-bottom: 2px;
  }
  .body-text { font-size: 14px; line-height: 17px; }
  .body-text + .body-text { margin-top: 4px; }

  .section-one { top: 252px; }
  .section-two { top: 411px; }

  .bullet-list { top: 636px; left: 96px; list-style: none; font-size: 14px; line-height: 17.2px; }
  .bullet-list li { position: relative; padding-left: 16px; }
  .bullet-list li::before {
    content: ""; position: absolute; left: 0; top: 6px;
    width: 5px; height: 5px; border-radius: 50%; background: var(--brand-blue);
  }

  .quote-block { top: 751px; font-style: italic; }

  .table-caption {
    top: 833px; text-align: center; color: var(--brand-blue);
    font-style: italic; font-size: 15px; line-height: 18px;
  }
  .data-table {
    position: absolute; top: 857px; left: 91px; width: 667px;
    border-collapse: collapse; font-size: 13px; table-layout: fixed;
  }
  .data-table th, .data-table td { border: 1px solid var(--rule); height: 21px; padding: 0; }
  .data-table th { background: var(--brand-blue); font-weight: 400; text-align: center; border-color: var(--rule); }
  .data-table td { text-align: left; padding-left: 25px; }

  .closing-one { top: 960px; }
  .closing-two { top: 1045px; }
  .indented { text-indent: 19px; }

  .footer-rule { position: absolute; top: 1142px; left: 0; width: 848px; height: 2px; background: var(--brand-red); }
  .page-number {
    position: absolute; left: 32px; top: 1141px; width: 19px; height: 19px;
    background: var(--paper); border: 1.5px solid var(--brand-red); transform: rotate(45deg);
  }
  .page-number span {
    position: absolute; inset: 0; display: flex; align-items: center; justify-content: center;
    transform: rotate(-45deg); font-size: 10px; color: var(--ink);
  }
</style>
</head>
<body>
<div class="page">
  <div class="header-rule red left"></div>
  <div class="header-rule blue left"></div>
  <div class="header-rule red right"></div>
  <div class="header-rule blue right"></div>
  <div class="brand"><span class="brand-dot"></span><span class="brand-name">Pelo Minis</span></div>

  <h1 class="block doc-title">Lorem ipsum dolor sit amet</h1>
  <h2 class="block doc-subtitle">Lorem ipsum dolor sit amet</h2>

  <section class="block section-one">
    <h3 class="section-heading">Lorem ipsum dolor sit amet</h3>
    <p class="body-text">Lorem ipsum dolor sit amet, consectetur meri odipiscing elit Mauris pretium porta turpis, semper ornare magna elementum convallis.</p>
    <p class="body-text">Aliquam malesuada dolor eros, nec fermentum massa commodo eu. NuLLa feLis purus, tincidunt nec uLtrices a, dictum a mauris. Maecenas Lorem augue, pellentesque pulvinar quam a, pretium finibus magna. Quisque dapibus voLutpat massa nec vestibulum. Ut porttitor ultricies magna vitae iaculis.</p>
    <p class="body-text">Suspendisse vel faucibus diam, dapibus peLLentesque quam. Maecenas eu varius nulla. PeLLentesque ornare tortor et pharetra peLLentesque. Nam in elementum ante.</p>
  </section>

  <section class="block section-two">
    <h3 class="section-heading">Lorem ipsum dolor sit amet</h3>
    <p class="body-text">Nulla sodales eros et quam gravida molestie. Muspendisse sit amet pharetra dui.</p>
    <p class="body-text">Quisque sit amet rhoncus dolor. Praesent euismod feLis nuLLa, sed sodales enim vehicula eu. Integer vestibuLum accumsan ligula, eget malesuada Lacus porttitor porta.</p>
    <p class="body-text">Donee tincidunt enim et peLLentesque consequat. ALiquam vitae velit Lectus. Nam arcu vitae tortor Luctus, quis maLesuada metus rhoncus. Quisque ornare Lectus sed finibus condimentum. In at suscipit tortor, nec aLiquet est. Suspendisse potenti. Sed finibus veLit ipsum, a fermentum. PhaseLLus nec. Proin dignissim, nuLLa veL vehicuLa hendrerit, arcu urna sceLerisque nisL, non porta purus tortor in orci.</p>
    <p class="body-text">Nulla lorem eros, hendrerit a mattis vel, elementum aliquam nisi. Etiam vel sapien mi. Cros nec varius ipsum. Interdum et malesuada fames ac ante ipsum primis in faucibus.</p>
  </section>

  <ul class="block bullet-list">
    <li>Proin euismod lobortis lacinia.</li>
    <li>Proin euismod lobortis lacinia.</li>
    <li>Proin euismod lobortis lacinia.</li>
    <li>Proin euismod lobortis lacinia.</li>
    <li>Proin euismod lobortis lacinia.</li>
  </ul>

  <section class="block quote-block">
    <p class="body-text">Etiam commodo, lacus enim lacinla lorem urna sit amet nibh.</p>
    <p class="body-text">Aliquam malesuada dolor eros, nec fermentum massa commodo eu. NuLLa feLis purus, tincidunt nec uLtrices a, dictum a mauris. Maecenas Lorem augue, pellentesque pulvinar quam a, pretium finibus magna. Quisque dapibus voLutpat massa nec vestibulum. Ut porttitor ultricies magna vitae iaculis.</p>
  </section>

  <p class="block table-caption">Lorem ipsum dolor sit amet</p>
  <table class="data-table">
    <thead>
      <tr><th>Nunc nec Leo</th><th>venenatis LiguLa</th><th>tempus Lectus</th><th>Proin faciLisis</th></tr>
    </thead>
    <tbody>
      <tr><td>Curabitur pretium</td><td>Curabitur pretium</td><td>Curabitur pretium</td><td>Curabitur pretium</td></tr>
      <tr><td>Curabitur pretium</td><td>Curabitur pretium</td><td>Curabitur pretium</td><td>Curabitur pretium</td></tr>
      <tr><td>Curabitur pretium</td><td>Curabitur pretium</td><td>Curabitur pretium</td><td>Curabitur pretium</td></tr>
    </tbody>
  </table>

  <p class="block body-text indented closing-one">Nunc nec Leo iaculis, venenatis LiguLa eget, tempus Lectus. Proin faciLisis eras a sapien sodaLes sodaLes. Curabitur pretium sed massa sed porta. NuLLa quis dui at risus uLtricies iacuLis. Curabitur vel tortor sagittis, Lobortis lacus pLacerat, euismod nibh. Class aptent taciti sociosqu ad Litora torquent per conubia nostra, per inceptos himenaeos. Integer sit amet dignissim mi.</p>
  <p class="block body-text indented closing-two">Nunc nec Leo iaculis, venenatis LiguLa eget, tempus Lectus. Proin faciLisis eras a sapien sodaLes sodaLes. Curabitur pretium sed massa sed porta. NuLLa quis dui at risus uLtricies iacuLis. Curabitur vel tortor sagittis, Lobortis lacus pLacerat, euismod nibh. Class aptent taciti sociosqu ad Litora torquent per conubia nostra, per inceptos himenaeos. Integer sit amet dignissim mi. conubia nostra, per inceptos himenaeos. Integer sit amet dignissim mi.</p>

  <div class="footer-rule"></div>
  <div class="page-number"><span>12</span></div>
</div>
</body>
</html>
```